Software engineering company needs business card

I need a cool business card. Company: Soft Belan Brindlewood Ave 41 58207 Sincity Name: Gerald Vanholt CEO / Managing Director & Owner

```html
<!DOCTYPE html>
<html lang="en">
<head>
<meta charset="utf-8">
<title>Soft Belan – Business Card</title>
<link href="https://fonts.googleapis.com/css2?family=Open+Sans:wght@400;600&display=swap" rel="stylesheet">
<style>
  :root {
    --backdrop: #35261f;
    --card: #0c0c0c;
    --card-edge: #1b1b1b;
    --green: #8cc63f;
    --grey: #8a8a8a;
    --grey-light: #b4b4b4;
    --divider: #6b6b6b;
  }
  * { box-sizing: border-box; margin: 0; padding: 0; }
  html, body {
    width: 1200px; height: 1000px; overflow: hidden;
    background: var(--backdrop);
    font-family: "Open Sans", Arial, sans-serif;
  }
  .stage { position: relative; width: 1200px; height: 1000px; }
  .card {
    position: absolute;
    width: 520px; height: 296px;
    background: var(--card);
    border: 1px solid var(--card-edge);
    border-radius: 22px;
  }
  .card--front { left: 170px; top: 200px; display: flex; align-items: center; justify-content: center; }
  .card--back { left: 500px; top: 530px; }

  .front-wordmark {
    display: flex; align-items: center; gap: 16px;
    font-size: 44px; font-weight: 600; letter-spacing: 2px;
    color: var(--green);
  }
  .front-wordmark .mark-square { width: 22px; height: 22px; background: var(--grey); }

  .back-wordmark {
    position: absolute; left: 28px; top: 132px; width: 200px;
    text-align: center;
    font-size: 21px; font-weight: 600; letter-spacing: 2px;
    color: var(--green);
  }
  .divider {
    position: absolute; left: 248px; top: 75px;
    width: 1px; height: 146px; background: var(--divider);
  }
  .details { position: absolute; left: 268px; top: 70px; }
  .details .person-name { font-size: 22px; font-weight: 600; color: var(--grey-light); line-height: 1.2; }
  .details .person-name .surname { color: var(--green); }
  .details .person-role { font-size: 13px; color: var(--grey); margin-top: 2px; }
  .details .contact { margin-top: 16px; font-size: 13px; line-height: 17px; color: var(--grey-light); }
  .details .address { margin-top: 12px; font-size: 13px; line-height: 17px; color: var(--green); }
</style>
</head>
<body>
<div class="stage">
  <section class="card card--front" aria-label="Card front">
    <div class="front-wordmark"><span class="mark-square"></span>Soft Belan</div>
  </section>

  <section class="card card--back" aria-label="Card back">
    <div class="back-wordmark">Soft Belan</div>
    <div class="divider"></div>
    <div class="details">
      <p class="person-name">Gerald <span class="surname">Vanholt</span></p>
      <p class="person-role">CEO / Geschäftsführer &amp; Inhaber</p>
      <p class="contact">+12 456 987 3012<br>gerald@belanmail.com<br>www.softbelan.com</p>
      <p class="address">Soft Belan, Brindlewood Ave 41<br>58207 Sincity</p>
    </div>
  </section>
</div>
</body>
</html>
```